Plakate für Podologie - Medizinische Fusspflege
Zielgruppe
Podologie - Medizinische Fusspflege. Zielgruppe sind Kinder bis und mit ältere Menschen.
Aufgabenstellung
Möchte ein modernes, aber auch klassisches Design, dass Professionalität & medizinische Fundiertheit ausstrahlt. Man soll sehen, dass es medizinisch ist und nicht verwechselbar mit kosmetischer Fusspflege.

```html
<!DOCTYPE html>
<html lang="de">
<head>
<meta charset="utf-8">
<title>Pedalis – Medizinische Podologie</title>
<link rel="stylesheet" href="https://fonts.googleapis.com/css2?family=Poppins:wght@400;500;700;800&display=swap">
<style>
  :root {
    --teal: #155e58;
    --teal-deep: #135954;
    --green: #6aa84f;
    --mint: #e1efe1;
    --ink: #111111;
    --grey: #6b6b6b;
    --paper: #ffffff;
    --backdrop: #ebebeb;
  }
  * { margin: 0; padding: 0; box-sizing: border-box; }
  html, body {
    width: 1200px; height: 960px; overflow: hidden;
    background: var(--backdrop);
    font-family: "Poppins", sans-serif;
  }
  .poster {
    position: absolute; left: 306px; top: 46px;
    width: 613px; height: 868px;
    background: var(--paper);
    overflow: hidden;
  }
  .waves { position: absolute; left: 0; top: 0; width: 613px; height: 868px; }
  .brand {
    position: absolute; left: 0; right: 0; top: 52px;
    display: flex; justify-content: center; align-items: center; gap: 14px;
  }
  .brand-dot { width: 46px; height: 46px; border-radius: 50%; background: var(--teal); }
  .brand-text { display: flex; flex-direction: column; }
  .brand-name { font-size: 40px; font-weight: 500; color: var(--teal); line-height: 1; letter-spacing: -0.5px; }
  .brand-tag { font-size: 10.5px; color: var(--grey); letter-spacing: 2px; margin-top: 6px; }
  .headline {
    position: absolute; left: 0; right: 0; top: 152px;
    text-align: center; font-size: 33px; font-weight: 800; color: var(--teal); letter-spacing: -0.2px;
  }
  .lead {
    position: absolute; left: 0; right: 0; top: 198px;
    text-align: center; font-size: 21px; line-height: 32px; color: var(--ink);
  }
  .services { position: absolute; left: 96px; top: 285px; width: 421px; list-style: none; }
  .service { position: relative; height: 66.5px; }
  .service-icon {
    position: absolute; left: 0; top: 0; width: 54px; height: 54px;
    border-radius: 10px; background: var(--mint);
  }
  .service-label {
    position: absolute; left: 84px; top: 13px;
    font-size: 20px; font-weight: 700; color: var(--teal); white-space: nowrap;
  }
  .service + .service::before {
    content: ""; position: absolute; left: 84px; right: 0; top: -7px;
    border-top: 1.5px solid var(--teal);
  }
  .cta {
    position: absolute; left: 118px; top: 630px; width: 377px; height: 58px;
    border-radius: 29px; background: var(--green); color: var(--paper);
    font-size: 23px; font-weight: 700; display: flex; align-items: center; justify-content: center;
  }
  .contact {
    position: absolute; left: 0; right: 0; top: 803px;
    text-align: center; font-size: 18px; color: var(--paper);
  }
</style>
</head>
<body>
  <main class="poster">
    <svg class="waves" viewBox="0 0 613 868" aria-hidden="true">
      <path fill="var(--green)" d="M70 704 C180 760 330 752 430 738 C520 726 580 740 613 765 L613 868 L0 868 Z"/>
      <path fill="var(--teal-deep)" d="M0 564 C15 640 40 690 70 704 C180 752 300 770 420 780 C520 790 590 820 613 868 L0 868 Z"/>
    </svg>

    <header class="brand">
      <span class="brand-dot"></span>
      <div class="brand-text">
        <span class="brand-name">Pedalis</span>
        <span class="brand-tag">MEDIZINISCHE PODOLOGIE</span>
      </div>
    </header>

    <h1 class="headline">Ihre Füsse. Unsere Kompetenz</h1>
    <p class="lead">Medizinische Fussbehandlungen für Ihre<br>Gesundheit und Lebensqualität.</p>

    <ul class="services">
      <li class="service"><span class="service-icon" role="img" aria-label="Symbol: zwei Fussabdrücke"></span><span class="service-label">Medizinische Fusspflege</span></li>
      <li class="service"><span class="service-icon" role="img" aria-label="Symbol: Zehennagel mit Korrekturpfeilen"></span><span class="service-label">Nagelkorrektur</span></li>
      <li class="service"><span class="service-icon" role="img" aria-label="Symbol: eingewachsener Zehennagel"></span><span class="service-label">Eingewachsene Nägel</span></li>
      <li class="service"><span class="service-icon" role="img" aria-label="Symbol: Hornhaut und Hühneraugen"></span><span class="service-label">Hornhaut &amp;Hühneraugen</span></li>
      <li class="service"><span class="service-icon" role="img" aria-label="Symbol: Fuss mit Blutstropfen"></span><span class="service-label">Diabetische Fussversorgung</span></li>
    </ul>

    <div class="cta">Jetzt Termin vereinbaren</div>

    <footer class="contact">Telefonnummer XXX | pedalis.ch | Adresse XXX</footer>
  </main>
</body>
</html>
```